Design a business card
Business name: Kestrel Yield Consulting
Improving Business Profitibility

- An Overview of the Business & Service:

Business Performance Consulting

- The Target Market: Small to medium-sized business

- Design Specifics:
White card, blue ink, moon eclipse

No Logo

Target Market(s)

Small to medium-sized business

Font styles to use
Sans Serif

```html
<!DOCTYPE html>
<html lang="en">
<head>
<meta charset="utf-8">
<title>Kestrel Yield Consulting — Business Card</title>
<link rel="stylesheet" href="https://fonts.googleapis.com/css2?family=Libre+Caslon+Text:wght@400;700&family=Questrial&display=swap">
<style>
  :root {
    --page-bg: #e7e6e3;
    --card-white: #f7f7f8;
    --card-edge: #d9dade;
    --ink-navy: #1d3a63;
    --ink-dark: #2e2e30;
    --ink-body: #1f1f22;
    --rule-navy: #1c2a5e;
    --band-deep: #2f3852;
    --band-mid: #4a5573;
    --band-light: #66708d;
    --wave-silver: #d4d5dc;
  }
  html, body {
    margin: 0;
    padding: 0;
    width: 1200px;
    height: 970px;
    overflow: hidden;
    background: var(--page-bg);
  }
  .canvas {
    position: relative;
    width: 1200px;
    height: 970px;
  }
  .business-card {
    position: absolute;
    left: 100px;
    top: 209px;
    width: 1000px;
    height: 552px;
    background: linear-gradient(180deg, #fbfbfc 0%, var(--card-white) 60%, #efeff2 100%);
    border: 1px solid var(--card-edge);
    box-shadow: 0 10px 30px rgba(0,0,0,0.12);
    overflow: hidden;
  }
  .wordmark {
    position: absolute;
    left: 62px;
    top: 142px;
    width: 420px;
    margin: 0;
    font-family: "Libre Caslon Text", Georgia, serif;
    font-weight: 400;
    color: var(--ink-navy);
    text-align: center;
  }
  .wordmark-main {
    display: block;
    font-size: 86px;
    line-height: 86px;
    letter-spacing: 1px;
  }
  .wordmark-sub {
    display: block;
    font-size: 35px;
    line-height: 38px;
    margin-top: 2px;
  }
  .person-name {
    position: absolute;
    left: 62px;
    top: 280px;
    width: 420px;
    margin: 0;
    text-align: center;
    font-family: "Libre Caslon Text", Georgia, serif;
    font-weight: 400;
    font-size: 31px;
    color: var(--ink-dark);
  }
  .divider {
    position: absolute;
    left: 534px;
    top: 98px;
    width: 3px;
    height: 262px;
    background: var(--rule-navy);
  }
  .contact-list {
    position: absolute;
    left: 620px;
    top: 158px;
    margin: 0;
    padding: 0;
    list-style: none;
    font-family: "Questrial", "Century Gothic", sans-serif;
    font-size: 22px;
    color: var(--ink-body);
  }
  .contact-item {
    position: relative;
    padding-left: 34px;
    line-height: 26px;
    margin-bottom: 11px;
  }
  .contact-icon {
    position: absolute;
    left: 0;
    top: 3px;
    width: 20px;
    height: 20px;
  }
  .wave-band {
    position: absolute;
    left: 0;
    top: 0;
    width: 1000px;
    height: 552px;
  }
</style>
</head>
<body>
<div class="canvas">
  <div class="business-card">

    <svg class="wave-band" viewBox="0 0 1000 552" role="img" aria-label="Moon surface texture in deep blue-grey filling the wave band">
      <defs>
        <linearGradient id="moonTone" x1="0" y1="0" x2="1" y2="1">
          <stop offset="0" stop-color="var(--band-deep)"/>
          <stop offset="0.45" stop-color="var(--band-mid)"/>
          <stop offset="0.75" stop-color="var(--band-light)"/>
          <stop offset="1" stop-color="var(--band-mid)"/>
        </linearGradient>
      </defs>
      <path d="M0,427 C160,450 300,470 470,445 C640,418 760,390 880,405 C940,413 975,430 1000,456 L1000,552 L0,552 Z" fill="url(#moonTone)"/>
      <path d="M0,473 C200,492 380,490 560,460 C720,432 820,405 900,418 C950,426 980,440 1000,448" fill="none" stroke="var(--wave-silver)" stroke-width="4"/>
    </svg>

    <h1 class="wordmark">
      <span class="wordmark-main">KESTREL</span>
      <span class="wordmark-sub">Yield Consulting</span>
    </h1>
    <p class="person-name">Desmond R Hale</p>

    <div class="divider"></div>

    <ul class="contact-list">
      <li class="contact-item">
        <svg class="contact-icon" viewBox="0 0 20 20" aria-hidden="true">
          <rect x="5" y="1" width="10" height="18" rx="1.5" fill="none" stroke="var(--ink-navy)" stroke-width="1.6"/>
          <rect x="7" y="4" width="6" height="7" fill="var(--ink-navy)"/>
          <circle cx="10" cy="15.5" r="1.2" fill="var(--ink-navy)"/>
        </svg>
        (415) 555-0192
      </li>
      <li class="contact-item">
        <svg class="contact-icon" viewBox="0 0 20 20" aria-hidden="true">
          <path d="M4 2 L7.5 2 L9 6.5 L6.8 8 C7.8 10.4 9.6 12.2 12 13.2 L13.5 11 L18 12.5 L18 16 C18 17.2 17 18 15.8 18 C8.2 17.5 2.5 11.8 2 4.2 C2 3 2.8 2 4 2 Z" fill="var(--ink-navy)"/>
          <path d="M11 2.5 A6.5 6.5 0 0 1 17.5 9" fill="none" stroke="var(--ink-navy)" stroke-width="1.5"/>
          <path d="M11 5.5 A3.5 3.5 0 0 1 14.5 9" fill="none" stroke="var(--ink-navy)" stroke-width="1.5"/>
        </svg>
        (415) 555-0192
      </li>
      <li class="contact-item">
        <svg class="contact-icon" viewBox="0 0 20 20" aria-hidden="true">
          <path d="M10 1 C6.4 1 3.8 3.7 3.8 7.2 C3.8 11.6 10 19 10 19 C10 19 16.2 11.6 16.2 7.2 C16.2 3.7 13.6 1 10 1 Z" fill="var(--ink-navy)"/>
          <circle cx="10" cy="7.2" r="2.4" fill="var(--card-white)"/>
        </svg>
        482 Harbor Ln.<br>Fairview Oregon 97024
      </li>
    </ul>

  </div>
</div>
</body>
</html>
```